Design some Business Card for shipping company

We need a creative business card designed for a shipping company. All relevant information such as address and phone number can be found on our website. Will need a design for both front and back. The front will container our logo, slogan, contact information etc. The back will have a coupon and some text. check out www.talvorfreight.example for all the information. We need something memorable and unique that will stand out. It needs to a horizontal design. Not vertical.

```html
<!DOCTYPE html>
<html lang="en">
<head>
<meta charset="utf-8">
<title>Talvor Freight business card</title>
<link href="https://fonts.googleapis.com/css2?family=Open+Sans:wght@400;600;700&display=swap" rel="stylesheet">
<style>
  :root {
    --red: #c8202f;
    --red-dark: #a3141f;
    --green: #17944a;
    --ink: #2b2b2b;
    --grey: #5a5a5a;
    --paper: #ffffff;
    --backdrop: #e9e7e3;
  }
  * { margin: 0; padding: 0; box-sizing: border-box; }
  html, body { width: 1200px; height: 1023px; overflow: hidden; }
  body {
    background: var(--backdrop);
    font-family: "Open Sans", Arial, sans-serif;
    color: var(--ink);
    position: relative;
  }
  .card {
    position: absolute;
    left: 220px;
    width: 760px;
    height: 434px;
    border-radius: 22px;
    background: var(--paper);
    box-shadow: 0 6px 18px rgba(0,0,0,.18);
    overflow: hidden;
  }
  .card--front { top: 50px; }
  .card--back { top: 539px; background: linear-gradient(160deg, #ffffff 0%, #ececec 100%); }

  .wave { position: absolute; inset: 0; width: 100%; height: 100%; }

  .brand { position: absolute; display: flex; align-items: center; gap: 12px; }
  .brand__dot { width: 34px; height: 34px; border-radius: 50%; background: var(--red); flex: none; }
  .brand__name { font-weight: 700; font-size: 30px; color: var(--red); text-transform: uppercase; letter-spacing: .5px; line-height: 1; }
  .brand__slogan { font-weight: 700; font-size: 13px; color: var(--ink); margin-top: 5px; }

  .card--front .brand { left: 250px; top: 60px; }

  .person { position: absolute; left: 44px; top: 200px; }
  .person__name { font-size: 34px; font-weight: 400; color: var(--ink); line-height: 1.1; }
  .person__role { font-size: 17px; color: var(--red); margin-top: 4px; }

  .phones { position: absolute; left: 44px; top: 292px; font-size: 15px; color: var(--grey); }
  .phones__group { display: grid; grid-template-columns: 80px 22px auto; row-gap: 6px; column-gap: 8px; align-items: center; margin-bottom: 10px; }
  .phones__region { grid-row: span 2; }
  .icon { width: 16px; height: 16px; flex: none; }

  .contact { position: absolute; right: 40px; top: 132px; font-size: 15px; color: var(--grey); }
  .contact__row { display: flex; align-items: center; gap: 10px; margin-bottom: 8px; }

  .tagline { position: absolute; right: 40px; top: 300px; font-size: 18px; color: #fff; }

  .card--back .brand { left: 50%; top: 60px; transform: translateX(-50%); }
  .about {
    position: absolute; left: 70px; right: 70px; top: 170px;
    font-size: 19px; line-height: 1.55; color: var(--ink); text-align: justify;
  }
</style>
</head>
<body>

<section class="card card--front" aria-label="Card front">
  <svg class="wave" viewBox="0 0 760 434" preserveAspectRatio="none" aria-hidden="true">
    <path d="M300 434 C 420 320, 510 250, 760 200 L760 434 Z" fill="var(--green)"/>
    <path d="M322 434 C 440 328, 525 264, 760 216 L760 434 Z" fill="#ffffff"/>
    <path d="M340 434 C 458 336, 540 278, 760 232 L760 434 Z" fill="var(--red)"/>
    <path d="M560 434 C 640 370, 700 330, 760 310 L760 434 Z" fill="var(--red-dark)" opacity=".35"/>
  </svg>

  <div class="brand">
    <span class="brand__dot"></span>
    <div>
      <div class="brand__name">Talvor Freight</div>
      <div class="brand__slogan">Secure Affordable Shipping to Kenya</div>
    </div>
  </div>

  <div class="person">
    <div class="person__name">Daniel Orwa</div>
    <div class="person__role">Managing Director</div>
  </div>

  <div class="phones">
    <div class="phones__group">
      <span class="phones__region">usa</span>
      <svg class="icon" viewBox="0 0 16 16"><path d="M3 1.5l3 3-1.5 2c1 2 2.5 3.5 4.5 4.5l2-1.5 3 3-2 2C7 14 2 9 1.5 3.5z" fill="var(--green)"/></svg>
      <span>+1 555 010 4074</span>
      <svg class="icon" viewBox="0 0 16 16"><rect x="4" y="1" width="8" height="14" rx="1.5" fill="none" stroke="var(--green)" stroke-width="1.6"/></svg>
      <span>+1 555 013 7322</span>
    </div>
    <div class="phones__group">
      <span class="phones__region">kenya</span>
      <svg class="icon" viewBox="0 0 16 16"><path d="M3 1.5l3 3-1.5 2c1 2 2.5 3.5 4.5 4.5l2-1.5 3 3-2 2C7 14 2 9 1.5 3.5z" fill="var(--green)"/></svg>
      <span>+254 700 100 555</span>
      <svg class="icon" viewBox="0 0 16 16"><rect x="4" y="1" width="8" height="14" rx="1.5" fill="none" stroke="var(--green)" stroke-width="1.6"/></svg>
      <span>+254 700 200 737</span>
    </div>
  </div>

  <div class="contact">
    <div class="contact__row">
      <svg class="icon" viewBox="0 0 16 16"><rect x="1" y="3" width="14" height="10" fill="var(--green)"/><path d="M1 3l7 6 7-6" fill="none" stroke="#fff" stroke-width="1.3"/></svg>
      <span>info@talvorfreight.example</span>
    </div>
    <div class="contact__row">
      <svg class="icon" viewBox="0 0 16 16"><circle cx="8" cy="8" r="7" fill="var(--green)"/><path d="M1 8h14M8 1c-3 3-3 11 0 14M8 1c3 3 3 11 0 14" fill="none" stroke="#fff" stroke-width="1"/></svg>
      <span>www.talvorfreight.example</span>
    </div>
  </div>

  <div class="tagline">USA to KENYA shipping</div>
</section>

<section class="card card--back" aria-label="Card back">
  <div class="brand">
    <span class="brand__dot"></span>
    <div>
      <div class="brand__name">Talvor Freight</div>
      <div class="brand__slogan">Secure Affordable Shipping to Kenya</div>
    </div>
  </div>
  <p class="about">Fast, secure and reliable ocean shipping service to Kenya from the USA. Our rates include customs and duty all the way to our warehouse in Nairobi. Packages are picked up from our Mombasa rd warehouse. Door to door delivery also available. All prices are based on volume. Weight does not matter. Free package pick up in the Seattle area</p>
</section>

</body>
</html>
```